Business card design for event company

need design double sided in square shape ( approx 6x6cm) in matt grey shades
front side :
logo ( could be in one color like picture attached ) printpress effect in a rect box

back side :
name in big font with silver foil finish ( similar to attached pic )

phone number i would like to see how it will look like if embossed ( like in credit cards )

Sample for contact on card ( will need 5 different contacts) - pls. include small icons next to each contact

KARIM SALEHI
Managing Director

+971 50 374 6619
karim@novlinkuae.com
www.novlink.ae
Building C2 , Office 318
Marsa Tirel Park

Please consider this is an urgent project . thank you in advance

```html
<!DOCTYPE html>
<html lang="en">
<head>
<meta charset="utf-8">
<title>Novlink — Business Card</title>
<link href="https://fonts.googleapis.com/css2?family=Roboto:wght@400;500;700&family=Roboto+Condensed:wght@500&display=swap" rel="stylesheet">
<style>
  :root {
    --page-bg: #e6e2dc;
    --card-bg: #f4f4f4;
    --ink-dark: #4a4a4a;
    --ink-mid: #555555;
    --accent: #f39323;
  }
  * { margin: 0; padding: 0; box-sizing: border-box; }
  html, body { width: 1200px; height: 960px; overflow: hidden; }
  body {
    background: var(--page-bg);
    position: relative;
    font-family: "Roboto", sans-serif;
    color: var(--ink-mid);
  }
  .card {
    position: absolute;
    width: 354px;
    height: 343px;
    background: var(--card-bg);
    box-shadow: 0 3px 8px rgba(0,0,0,0.25);
  }
  .card--front { left: 437px; top: 113px; }
  .card--back  { left: 434px; top: 472px; }

  .brand {
    position: absolute;
    display: flex;
    align-items: center;
    gap: 10px;
  }
  .brand__mark {
    width: 14px; height: 14px;
    background: var(--accent);
  }
  .brand__name {
    font-family: "Roboto", sans-serif;
    font-weight: 500;
    font-size: 40px;
    line-height: 1;
    color: var(--ink-dark);
    letter-spacing: 0.5px;
  }
  .card--front .brand { left: 49px; top: 52px; }
  .card--back .brand { left: 0; right: 0; top: 156px; justify-content: center; }

  .person { position: absolute; left: 49px; top: 130px; }
  .person__name {
    font-family: "Roboto Condensed", sans-serif;
    font-weight: 500;
    font-size: 21px;
    color: var(--accent);
    line-height: 1;
  }
  .person__title {
    font-weight: 500;
    font-size: 15px;
    color: var(--ink-mid);
    margin-top: 7px;
    letter-spacing: 0.2px;
  }
  .address {
    position: absolute; left: 49px; top: 185px;
    font-size: 14px; line-height: 19px; color: var(--ink-mid);
  }
  .contacts {
    position: absolute; left: 50px; top: 236px;
    list-style: none; font-size: 14px; line-height: 20px;
  }
  .contacts li { display: flex; align-items: center; gap: 6px; }
  .contacts svg { width: 13px; height: 13px; fill: var(--accent); flex: none; }

  .back-web {
    position: absolute; left: 0; right: 0; top: 305px;
    text-align: center; font-size: 14px; letter-spacing: 1.2px; color: var(--ink-mid);
  }
  .back-web strong { font-weight: 700; color: var(--ink-dark); }
</style>
</head>
<body>
  <section class="card card--front">
    <div class="brand">
      <span class="brand__name">Novlink</span>
      <span class="brand__mark"></span>
    </div>
    <div class="person">
      <div class="person__name">KARIM SALEHI</div>
      <div class="person__title">MANAGING DIRECTOR</div>
    </div>
    <div class="address">
      Building C2 , Office 318<br>
      Marsa Tirel Park
    </div>
    <ul class="contacts">
      <li>
        <svg viewBox="0 0 24 24"><path d="M6.6 10.8a15.1 15.1 0 0 0 6.6 6.6l2.2-2.2c.3-.3.7-.4 1-.2 1.1.4 2.3.6 3.6.6.6 0 1 .4 1 1V20c0 .6-.4 1-1 1A17 17 0 0 1 3 4c0-.6.4-1 1-1h3.5c.6 0 1 .4 1 1 0 1.3.2 2.5.6 3.6.1.3 0 .7-.2 1z"/></svg>
        +971 50 374 6619
      </li>
      <li>
        <svg viewBox="0 0 24 24"><path d="M2 5h20v2l-10 6L2 7z"/><path d="M2 9l10 6 10-6v10H2z"/></svg>
        karim@novlinkuae.com
      </li>
      <li>
        <svg viewBox="0 0 24 24"><circle cx="12" cy="12" r="10"/></svg>
        www.novlink.ae
      </li>
    </ul>
  </section>

  <section class="card card--back">
    <div class="brand">
      <span class="brand__name">Novlink</span>
      <span class="brand__mark"></span>
    </div>
    <div class="back-web">www.<strong>novlink</strong>.ae</div>
  </section>
</body>
</html>
```